Halvery Building Group Website

Need a dynamic corporate website that can be built on with time. We want to get our information out to the world and have a place where customers can submit requests for proposals.

Target Market(s)

Custom home owners and buyers. Architects and Real Estate Agents.

Industry/Entity Type

Construction

Number of Pages Required

3 page

Font styles to use
Serif
Sans Serif

Requirements
Must have
• Company logo, about, company contact information, biography, contact, projects,
• Sleek, modern, clean, attractive design.
• Online form customers can use for filling out a request for project proposal.
• Workcircle hyperlink.
• Uses www.halverybuildinggroup.example

```html
<!DOCTYPE html>
<html lang="en">
<head>
<meta charset="utf-8">
<title>Halvery Building Group, Inc.</title>
<link rel="stylesheet" href="https://fonts.googleapis.com/css2?family=Raleway:wght@400;500;600&family=Open+Sans:wght@400;600;700&display=swap">
<style>
:root{
  --brand:#0b4f9d;
  --brand-deep:#283580;
  --brand-sky:#2f8fd0;
  --footer:#0a4e9e;
  --ink:#5f5f5f;
  --muted:#8a8a8a;
  --panel:#e4e4e4;
  --white:#ffffff;
}
*{margin:0;padding:0;box-sizing:border-box}
html,body{width:1200px;height:2222px;overflow:hidden;background:var(--white)}
body{position:relative;font-family:"Open Sans",Arial,sans-serif;color:var(--ink)}
.abs{position:absolute}

/* Hero */
.hero{left:0;top:0;width:1200px;height:667px;
  background:linear-gradient(180deg,#2c5f9a 0%,#8fb0c9 30%,#c9d7de 45%,#6f7f74 52%,#4d7c95 62%,#2f5f7c 80%,#1f4560 100%)}
.main-nav{left:77px;top:0;width:1046px;height:64px;border-bottom:1px solid rgba(255,255,255,.85)}
.main-nav a{position:absolute;top:24px;font-family:"Raleway",sans-serif;font-size:22px;color:var(--white);text-decoration:none;transform:translateX(-50%);letter-spacing:.3px}
.main-nav .active-bar{position:absolute;left:160px;top:56px;width:120px;height:4px;background:var(--white)}
.hero-name{left:0;top:262px;width:1200px;text-align:center;font-family:"Raleway",sans-serif;font-weight:600;font-size:50px;color:var(--brand);letter-spacing:1px}

/* Welcome */
.badge{left:540px;top:620px;width:120px;height:88px;background:var(--white);display:flex;align-items:center;justify-content:center;font-family:"Raleway",sans-serif;font-weight:600;font-size:22px;color:var(--brand)}
.welcome-kicker{left:0;top:733px;width:1200px;text-align:center;font-family:"Raleway",sans-serif;font-size:26px;color:var(--muted);letter-spacing:1px}
.welcome-title{left:0;top:765px;width:1200px;text-align:center;font-family:"Raleway",sans-serif;font-size:42px;color:var(--brand)}
.welcome-text{left:129px;top:837px;width:892px;text-align:center;font-size:15.5px;line-height:25px}

/* Services */
.service{top:944px;width:330px;text-align:center}
.service .disc{width:126px;height:126px;border-radius:50%;background:var(--brand);margin:0 auto;display:flex;align-items:center;justify-content:center}
.service h3{margin-top:26px;font-family:"Raleway",sans-serif;font-weight:500;font-size:27px;color:var(--brand)}
.service p{margin-top:6px;font-size:15.5px;line-height:25px}

/* Call band */
.call-band{left:77px;top:1241px;width:1046px;height:135px;background:var(--panel)}
.call-band svg{position:absolute;left:0;top:0}
.call-label{left:96px;top:1287px;font-family:"Raleway",sans-serif;font-size:27px;color:var(--white)}
.call-number{left:361px;top:1285px;font-weight:700;font-size:31px;color:var(--white)}
.call-icon{left:296px;top:1275px}
.call-text{left:631px;top:1256px;width:460px;font-size:15.5px;line-height:25px}
.call-mail{left:631px;top:1318px;font-size:18px;color:var(--brand);display:flex;align-items:center;gap:10px}

/* Projects */
.section-title{left:0;top:1418px;width:1200px;text-align:center;font-family:"Raleway",sans-serif;font-size:44px;color:var(--muted)}
.section-title span{color:var(--brand)}
.project{width:245px;height:162px}
.project-feature{background:linear-gradient(180deg,#1d6fb8,#0c57a3);color:var(--white);text-align:center;padding-top:26px}
.project-feature h4{font-weight:700;font-size:25px}
.project-feature p{font-size:15.5px;line-height:24px;padding:0 18px}
.view-all{left:523px;top:1881px;width:154px;height:46px;background:var(--brand);border-radius:3px;color:var(--white);font-family:"Raleway",sans-serif;font-size:22px;display:flex;align-items:center;justify-content:center;text-decoration:none}

/* Footer */
.site-footer{left:0;top:1984px;width:1200px;height:238px;background:var(--footer);color:var(--white)}
.footer-nav a{position:absolute;top:2005px;font-size:17px;color:var(--white);text-decoration:none}
.footer-rule{left:86px;top:2053px;width:1024px;height:1px;background:#3c79be}
.social{left:977px;top:1994px;display:flex;align-items:center;gap:14px;font-size:17px;color:var(--white)}
.round{width:46px;height:46px;border-radius:50%;background:var(--white);display:flex;align-items:center;justify-content:center}
.footer-heading{left:92px;top:2072px;font-size:21px;color:var(--white)}
.contact-item{top:2108px;display:flex;align-items:center;gap:12px;font-size:14px;line-height:24px;color:var(--white)}
.copyright{left:0;top:2177px;width:1200px;text-align:center;font-size:14px;color:var(--white)}
</style>
</head>
<body>

<header>
  <div class="abs hero" role="img" aria-label="Photograph of a city riverside skyline with a large observation wheel at dusk"></div>
  <nav class="abs main-nav">
    <a href="#" style="left:219px">HOME</a>
    <a href="#" style="left:350px">ABOUT</a>
    <a href="#" style="left:504px">PROJECTS</a>
    <a href="#" style="left:656px">NEWS</a>
    <a href="#" style="left:806px">CONTACT</a>
    <span class="active-bar"></span>
  </nav>
  <div class="abs hero-name">HALVERY BUILDING GROUP, INC.</div>
</header>

<main>
  <div class="abs badge">HALVERY</div>
  <p class="abs welcome-kicker">WELCOME TO</p>
  <h1 class="abs welcome-title" style="font-weight:400">HALVERY BUILDING GROUP, INC.</h1>
  <p class="abs welcome-text">Lorem Ipsum is simply dummy text of the printing and typesetting industry. Lorem Ipsum has been the industry's standard dummy text ever since the 1500s, when an unknown printer took a galley of type and scrambled it to make a type specimen book, It has survived not only five centuries.</p>

  <section class="abs service" style="left:75px">
    <div class="disc">
      <svg width="66" height="66" viewBox="0 0 66 66" fill="#fff">
        <rect x="8" y="24" width="14" height="36"/><rect x="24" y="8" width="18" height="52"/><rect x="44" y="30" width="14" height="30"/>
        <g fill="#0b4f9d"><rect x="28" y="14" width="4" height="5"/><rect x="35" y="14" width="4" height="5"/><rect x="28" y="24" width="4" height="5"/><rect x="35" y="24" width="4" height="5"/><rect x="28" y="34" width="4" height="5"/><rect x="35" y="34" width="4" height="5"/><rect x="12" y="30" width="6" height="4"/><rect x="12" y="40" width="6" height="4"/><rect x="48" y="36" width="6" height="4"/><rect x="48" y="46" width="6" height="4"/></g>
      </svg>
    </div>
    <h3>New Build</h3>
    <p>Lorem Ipsum is simply dummy text of the printing and typesetting industry. Lorem Ipsum has been the industry.</p>
  </section>
  <section class="abs service" style="left:435px">
    <div class="disc">
      <svg width="66" height="66" viewBox="0 0 66 66" fill="none" stroke="#fff" stroke-width="7" stroke-linecap="round">
        <line x1="14" y1="52" x2="46" y2="20"/><line x1="52" y1="52" x2="22" y2="22"/>
        <path d="M38 12 L54 12 L54 22" stroke-width="6"/><circle cx="18" cy="18" r="8" stroke-width="5"/>
      </svg>
    </div>
    <h3>Extension</h3>
    <p>Lorem Ipsum is simply dummy text of the printing and typesetting industry. Lorem Ipsum has been the industry.</p>
  </section>
  <section class="abs service" style="left:796px">
    <div class="disc">
      <svg width="66" height="66" viewBox="0 0 66 66" fill="#fff">
        <rect x="28" y="4" width="12" height="60" transform="rotate(-45 34 34)"/>
        <polygon points="14,10 48,44 44,52 10,18" />
        <polygon points="48,44 56,56 44,52" />
      </svg>
    </div>
    <h3>Refurbishments</h3>
    <p>Lorem Ipsum is simply dummy text of the printing and typesetting industry. Lorem Ipsum has been the industry.</p>
  </section>

  <aside class="abs call-band">
    <svg width="560" height="135" viewBox="0 0 560 135">
      <defs><linearGradient id="callFill" x1="0" y1="0" x2="0" y2="1"><stop offset="0" stop-color="#2a2f7e"/><stop offset="1" stop-color="#2f97d4"/></linearGradient></defs>
      <path d="M0 0 H547 Q572 68 547 135 H0 Z" fill="#fff"/>
      <path d="M0 0 H523 Q548 68 523 135 H0 Z" fill="url(#callFill)"/>
    </svg>
  </aside>
  <span class="abs call-label">CALL US NOW!</span>
  <svg class="abs call-icon" width="56" height="56" viewBox="0 0 56 56"><circle cx="28" cy="28" r="26" fill="none" stroke="#fff" stroke-width="2"/><path d="M20 16c2-1 4 0 5 3l1 4c0 2-1 3-3 4 1 3 4 6 7 7 1-2 2-3 4-3l4 1c3 1 4 3 3 5-1 3-4 4-7 3-8-2-14-8-16-16-1-3 0-6 2-8z" fill="#fff"/></svg>
  <span class="abs call-number">123 456 7890</span>
  <p class="abs call-text">Lorem Ipsum is simply dummy text of the printing and typesetting industry. Lorem Ipsum has been the industry.</p>
  <a class="abs call-mail"><svg width="20" height="15" viewBox="0 0 20 15" fill="none" stroke="#0b4f9d" stroke-width="2"><rect x="1" y="1" width="18" height="13"/><path d="M1 1l9 7 9-7"/></svg>info@halverybuildinggroup.example</a>

  <h2 class="abs section-title" style="font-weight:400">LATEST <span>PROJECT</span></h2>
  <div class="abs project" style="left:77px;top:1501px;background:linear-gradient(180deg,#f2efea,#d9d4cc)" role="img" aria-label="Photograph of a bright white living room"></div>
  <div class="abs project project-feature" style="left:344px;top:1501px"><h4>Project title</h4><p>Lorem Ipsum is simply dummy text of the printing and typesetting industry.</p></div>
  <div class="abs project" style="left:610px;top:1501px;background:linear-gradient(180deg,#2d6fb7,#8ab7dc 60%,#b9975d)" role="img" aria-label="Photograph of a construction site with a tower crane"></div>
  <div class="abs project" style="left:878px;top:1501px;background:linear-gradient(180deg,#b8c9d2,#e6ecef 60%,#9aa6ac)" role="img" aria-label="Photograph of a modern glass office interior"></div>
  <div class="abs project" style="left:77px;top:1684px;background:linear-gradient(180deg,#d7e2e6,#aeb8b8 55%,#4c5a3e)" role="img" aria-label="Photograph of a modern low pavilion house"></div>
  <div class="abs project" style="left:344px;top:1684px;background:linear-gradient(180deg,#cfdbe0,#eef2f3 60%,#a4acb0)" role="img" aria-label="Photograph of a glass-walled office interior"></div>
  <div class="abs project" style="left:610px;top:1684px;background:linear-gradient(180deg,#5aa2d8,#e8ecee 55%,#8a6a4a 80%,#6a8a4a)" role="img" aria-label="Photograph of a new two-storey house"></div>
  <div class="abs project" style="left:878px;top:1684px;background:linear-gradient(180deg,#3a86d0,#9fb6c8 50%,#5e8a3e)" role="img" aria-label="Photograph of suburban family houses"></div>
  <a class="abs view-all" href="#">VIEW ALL</a>
</main>

<footer class="abs site-footer"></footer>
<nav class="footer-nav">
  <a href="#" style="left:92px">Home</a>
  <a href="#" style="left:169px">About</a>
  <a href="#" style="left:246px">Projects</a>
  <a href="#" style="left:338px">News</a>
  <a href="#" style="left:410px">Contact</a>
</nav>
<a class="abs social"><span class="round"></span>Workcircle</a>
<div class="abs footer-rule"></div>
<h3 class="abs footer-heading" style="font-weight:400">Contact Us</h3>
<div class="abs contact-item" style="left:86px">
  <span class="round"><svg width="18" height="24" viewBox="0 0 18 24"><path d="M9 0a9 9 0 0 0-9 9c0 7 9 15 9 15s9-8 9-15a9 9 0 0 0-9-9z" fill="#0a4e9e"/><circle cx="9" cy="9" r="3.5" fill="#fff"/></svg></span>
  <span style="width:250px">Lorem Ipsum is dummy text of the printing.</span>
</div>
<div class="abs contact-item" style="left:446px;font-weight:700">
  <span class="round"><svg width="22" height="22" viewBox="16 14 28 28"><path d="M20 16c2-1 4 0 5 3l1 4c0 2-1 3-3 4 1 3 4 6 7 7 1-2 2-3 4-3l4 1c3 1 4 3 3 5-1 3-4 4-7 3-8-2-14-8-16-16-1-3 0-6 2-8z" fill="#0a4e9e"/></svg></span>
  123 456 7890
</div>
<div class="abs contact-item" style="left:799px;font-size:15px">
  <span class="round"><svg width="22" height="16" viewBox="0 0 20 15" fill="none" stroke="#0a4e9e" stroke-width="2"><rect x="1" y="1" width="18" height="13"/><path d="M1 1l9 7 9-7"/></svg></span>
  info@halverybuildinggroup.example
</div>
<p class="abs copyright">© <strong>HALVERY BUILDING GROUP, INC.</strong> - 2016. All Rights Reserved.</p>

</body>
</html>
```